Copper and Slate Mist NZ new website!

We are a new online vaping retailer and are looking for an awesome sleek website. We are going to be selling a variety of vaping products and gear. Our logo has just been developed and we would like to keep the website in line with the black, tan a white theme. We would like to trying watermarking or imposing the rottie into the background of the website on the home page, with the page being black and you can see the tan and white colours only.

Coding

Coded - Design and coding required

Number of Pages Required

2 page

Font styles to use
Serif
Sans Serif
Decorative

Requirements
Must have
• A home page and a standard page for products
• Stay in line with the colours in the logo

```html
<!DOCTYPE html>
<html lang="en">
<head>
<meta charset="utf-8">
<title>Copper and Slate Mist NZ</title>
<link href="https://fonts.googleapis.com/css2?family=Alfa+Slab+One&family=Montserrat:wght@400;500;600;700&display=swap" rel="stylesheet">
<style>
:root{
  --ink:#000;
  --band:#141414;
  --tan:#d4861f;
  --tan-soft:#b8741c;
  --white:#fff;
  --grey:#bdbdbd;
  --field:#0b0b0b;
  --line:#3a3a3a;
}
*{box-sizing:border-box;margin:0;padding:0}
html,body{width:1200px;height:3774px;overflow:hidden;background:var(--ink)}
body{position:relative;font-family:'Montserrat',sans-serif;color:var(--white)}
.abs{position:absolute}
.slab{font-family:'Alfa Slab One',serif;text-transform:uppercase}

/* hero */
.hero{left:0;top:0;width:1200px;height:700px;background:var(--ink)}
.hero-art{left:500px;top:0;width:560px;height:690px;background:radial-gradient(ellipse at 45% 50%,#3b3b3b 0%,#1a1a1a 45%,#000 75%)}
.brand{left:40px;top:40px;width:500px;height:500px;display:flex;align-items:center;gap:18px}
.brand-dot{width:46px;height:46px;border-radius:50%;background:var(--tan);flex:none}
.brand-name{font-family:'Montserrat',sans-serif;font-weight:700;font-size:34px;line-height:1.2;color:var(--tan)}
.topbar{left:578px;top:30px;display:flex;align-items:center;gap:24px;font-size:14px;color:var(--white)}
.topbar span{display:flex;align-items:center;gap:8px}
.social{display:flex;gap:6px}
.social i{width:20px;height:20px;border:1.5px solid var(--tan);border-radius:50%;display:block}
.menu{left:1093px;top:96px;width:46px}
.menu i{display:block;height:6px;background:var(--tan);border-radius:2px;margin-bottom:8px}
.hero-title{left:640px;top:250px;font-size:46px;line-height:1.15}
.hero-title .a{color:#d9d9d9}.hero-title .b{color:var(--tan)}

/* section headings */
.heading{left:0;width:1200px;text-align:center;font-size:38px;color:var(--tan);display:flex;justify-content:center;align-items:center;gap:14px}
.heading .dot{width:50px;height:50px;border-radius:50%;background:var(--tan-soft);border:3px solid #5a3a10}
.heading .w{color:var(--tan)}

/* products */
.product{width:244px;text-align:center}
.product .pic{width:221px;height:221px;margin:0 auto;border-radius:50%;border:5px solid var(--tan);padding:6px;background:var(--ink)}
.product .pic div{width:100%;height:100%;border-radius:50%}
.product .name{margin-top:30px;font-size:16px;color:var(--white)}
.product .meta{margin-top:14px;display:flex;justify-content:center;gap:26px;font-size:14px;color:var(--tan)}
.product .meta span{display:flex;align-items:center;gap:6px}
.coin{width:20px;height:20px;border:1.5px solid var(--tan);border-radius:50%;font-size:11px;display:flex;align-items:center;justify-content:center}
.arrow{width:20px;height:32px}

/* offer */
.offer{left:0;top:1218px;width:1200px;height:503px;background:#0d0d0d}
.offer-photo{left:0;top:0;width:680px;height:503px;background:radial-gradient(ellipse at 50% 45%,#4a4a4a 0%,#222 40%,#0d0d0d 80%)}
.offer-title{left:674px;top:128px;font-size:40px;line-height:1.27}
.offer-title .a{color:#a9a9a9}
.btn{border:2px solid var(--tan);border-radius:8px;color:var(--tan);font-family:'Alfa Slab One',serif;text-transform:uppercase;display:flex;align-items:center;justify-content:center;font-size:18px}

/* best sellers */
.sellers{left:0;top:1721px;width:1200px;height:564px;background:var(--band)}

/* about */
.about-copy{left:113px;top:2472px;width:620px;font-size:15.5px;line-height:1.55;color:#e6e6e6}
.about-copy p+p{margin-top:22px}
.about-photo{left:782px;top:2488px;width:328px;height:328px;border-radius:50%;border:6px solid var(--tan);padding:10px}
.about-photo div{width:100%;height:100%;border-radius:50%;background:linear-gradient(140deg,#9aa3ad 0%,#5b4a3a 55%,#1d1712 100%)}

/* contact */
.contact{left:0;top:2843px;width:1200px;height:541px;background:radial-gradient(ellipse at 35% 55%,#2a2a2a 0%,#1b1b1b 40%,#0f0f0f 100%)}
.field{height:50px;background:var(--field);border:1px solid var(--line);color:var(--white);font-size:17px;padding:12px 16px}

/* footer */
.footer{left:0;top:3384px;width:1200px;height:390px;background:#161616}
.foot-dot{left:93px;top:3460px;width:176px;height:176px;border-radius:50%;border:6px solid var(--tan);display:flex;align-items:center;justify-content:center;text-align:center;font-weight:700;font-size:17px;color:var(--tan);padding:18px}
.col h4{font-size:14px;font-weight:700;color:var(--tan);text-transform:uppercase;padding-bottom:8px;border-bottom:1px solid #555;width:110px}
.col ul{list-style:none;margin-top:12px;font-size:13px;line-height:21px;color:#e0e0e0}
.callbox{left:860px;top:3454px;width:247px;height:111px;border:2px solid var(--tan);border-radius:6px;text-align:center;padding-top:14px}
.callbox .t{font-size:14px;font-weight:700;color:var(--tan)}
.callbox .n{font-size:27px;font-weight:600;display:flex;justify-content:center;align-items:center;gap:8px;margin-top:2px}
.callbox .s{font-size:10px;color:var(--tan);margin-top:4px}
.rule{left:95px;top:3704px;width:1010px;height:1px;background:#444}
.copyright{left:0;top:3717px;width:1200px;text-align:center;font-size:11px;color:#aaa;letter-spacing:.5px}
</style>
</head>
<body>

<!-- hero -->
<section class="abs hero">
  <div class="abs hero-art" role="img" aria-label="Faint tan and white sketch of a standing rottweiler on black"></div>
  <div class="abs brand"><span class="brand-dot"></span><span class="brand-name">Copper and Slate<br>Mist NZ</span></div>
  <nav class="abs topbar">
    <span><svg width="18" height="18" viewBox="0 0 24 24"><path fill="#d4861f" d="M6.6 10.8a15 15 0 0 0 6.6 6.6l2.2-2.2a1 1 0 0 1 1-.25 11.4 11.4 0 0 0 3.6.6 1 1 0 0 1 1 1V20a1 1 0 0 1-1 1A17 17 0 0 1 3 4a1 1 0 0 1 1-1h3.5a1 1 0 0 1 1 1c0 1.25.2 2.45.6 3.6a1 1 0 0 1-.25 1z"/></svg>1800.555.0142</span>
    <span class="social"><i></i><i></i><i></i></span>
    <span><svg width="18" height="16" viewBox="0 0 24 20"><circle cx="9" cy="6" r="4.5" fill="#d4861f"/><path d="M1 19c0-5 4-7 8-7s8 2 8 7z" fill="#d4861f"/><path d="M19 5v6M16 8h6" stroke="#d4861f" stroke-width="2"/></svg>Register</span>
    <span><svg width="16" height="18" viewBox="0 0 20 24"><rect x="2" y="10" width="16" height="13" rx="2" fill="none" stroke="#d4861f" stroke-width="2"/><path d="M5 10V7a5 5 0 0 1 10 0v3" fill="none" stroke="#d4861f" stroke-width="2"/></svg>Log in</span>
    <span><svg width="20" height="18" viewBox="0 0 24 22"><path d="M1 2h4l3 12h12l3-9H7" fill="none" stroke="#d4861f" stroke-width="2"/><circle cx="10" cy="19" r="2" fill="#d4861f"/><circle cx="18" cy="19" r="2" fill="#d4861f"/></svg>Cart (0)</span>
  </nav>
  <div class="abs menu"><i></i><i></i><i></i></div>
  <h1 class="abs hero-title slab"><span class="a">We're all about</span><br><span class="b">High quality vape</span></h1>
</section>

<!-- shop now -->
<h2 class="abs heading slab" style="top:705px"><span class="dot"></span><span>Shop <span style="color:#c9791a">Now</span></span></h2>
<svg class="abs arrow" style="left:73px;top:902px" viewBox="0 0 20 32"><path d="M16 2 4 16l12 14" fill="none" stroke="#888" stroke-width="4"/></svg>
<svg class="abs arrow" style="left:1107px;top:902px" viewBox="0 0 20 32"><path d="M4 2l12 14L4 30" fill="none" stroke="#888" stroke-width="4"/></svg>

<div class="abs product" style="left:112px;top:808px"><div class="pic"><div role="img" aria-label="E-liquid bottle with box" style="background:linear-gradient(135deg,#e9e4d6,#6b7d3a 60%,#1c1c1c)"></div></div><div class="name">Ember Leaf Vape</div><div class="meta"><span><i class="coin">$</i>19.99</span><span><svg width="18" height="16" viewBox="0 0 24 22"><path d="M1 2h4l3 12h12l3-9H7" fill="none" stroke="#d4861f" stroke-width="2"/><circle cx="10" cy="19" r="2" fill="#d4861f"/><circle cx="18" cy="19" r="2" fill="#d4861f"/></svg>Buy Now</span></div></div>
<div class="abs product" style="left:356px;top:808px"><div class="pic"><div role="img" aria-label="Row of coloured vape pens" style="background:linear-gradient(90deg,#7a1f2a,#2a6e3a 30%,#2b3f8f 55%,#6b2d8a 80%,#333)"></div></div><div class="name">Ridge Vape Pen</div><div class="meta"><span><i class="coin">$</i>19.99</span><span><svg width="18" height="16" viewBox="0 0 24 22"><path d="M1 2h4l3 12h12l3-9H7" fill="none" stroke="#d4861f" stroke-width="2"/><circle cx="10" cy="19" r="2" fill="#d4861f"/><circle cx="18" cy="19" r="2" fill="#d4861f"/></svg>Buy Now</span></div></div>
<div class="abs product" style="left:600px;top:808px"><div class="pic"><div role="img" aria-label="E-liquid bottle on ice" style="background:radial-gradient(circle at 50% 55%,#f0f0f0,#8a8f96 50%,#151515)"></div></div><div class="name">Frost Drift Vape</div><div class="meta"><span><i class="coin">$</i>19.99</span><span><svg width="18" height="16" viewBox="0 0 24 22"><path d="M1 2h4l3 12h12l3-9H7" fill="none" stroke="#d4861f" stroke-width="2"/><circle cx="10" cy="19" r="2" fill="#d4861f"/><circle cx="18" cy="19" r="2" fill="#d4861f"/></svg>Buy Now</span></div></div>
<div class="abs product" style="left:839px;top:808px"><div class="pic"><div role="img" aria-label="Green e-liquid bottles" style="background:radial-gradient(circle at 50% 45%,#b8f03a,#4d9a1a 55%,#1a3a0a)"></div></div><div class="name">Orbit Lime Vape</div><div class="meta"><span><i class="coin">$</i>19.99</span><span><svg width="18" height="16" viewBox="0 0 24 22"><path d="M1 2h4l3 12h12l3-9H7" fill="none" stroke="#d4861f" stroke-width="2"/><circle cx="10" cy="19" r="2" fill="#d4861f"/><circle cx="18" cy="19" r="2" fill="#d4861f"/></svg>Buy Now</span></div></div>

<!-- special offer -->
<section class="abs offer">
  <div class="abs offer-photo" role="img" aria-label="Dark portrait photo with exhaled vapour cloud"></div>
  <h2 class="abs offer-title slab"><span class="a">Special offer</span><br>Get 20% off on your<br>purchase</h2>
  <a class="abs btn" style="left:674px;top:337px;width:237px;height:56px">Learn more</a>
</section>

<!-- best sellers -->
<section class="abs sellers"></section>
<h2 class="abs heading slab" style="top:1812px"><span class="dot"></span><span>Best <span style="color:#c9791a">Sellers</span></span></h2>
<svg class="abs arrow" style="left:73px;top:2009px" viewBox="0 0 20 32"><path d="M16 2 4 16l12 14" fill="none" stroke="#888" stroke-width="4"/></svg>
<svg class="abs arrow" style="left:1107px;top:2009px" viewBox="0 0 20 32"><path d="M4 2l12 14L4 30" fill="none" stroke="#888" stroke-width="4"/></svg>

<div class="abs product" style="left:112px;top:1915px"><div class="pic"><div role="img" aria-label="Green e-liquid bottles" style="background:radial-gradient(circle at 50% 45%,#b8f03a,#4d9a1a 55%,#1a3a0a)"></div></div><div class="name">Orbit Lime Vape</div><div class="meta"><span><i class="coin">$</i>19.99</span><span><svg width="18" height="16" viewBox="0 0 24 22"><path d="M1 2h4l3 12h12l3-9H7" fill="none" stroke="#d4861f" stroke-width="2"/><circle cx="10" cy="19" r="2" fill="#d4861f"/><circle cx="18" cy="19" r="2" fill="#d4861f"/></svg>Buy Now</span></div></div>
<div class="abs product" style="left:356px;top:1915px"><div class="pic"><div role="img" aria-label="E-liquid bottle on ice" style="background:radial-gradient(circle at 50% 55%,#f0f0f0,#8a8f96 50%,#151515)"></div></div><div class="name">Frost Drift Vape</div><div class="meta"><span><i class="coin">$</i>19.99</span><span><svg width="18" height="16" viewBox="0 0 24 22"><path d="M1 2h4l3 12h12l3-9H7" fill="none" stroke="#d4861f" stroke-width="2"/><circle cx="10" cy="19" r="2" fill="#d4861f"/><circle cx="18" cy="19" r="2" fill="#d4861f"/></svg>Buy Now</span></div></div>
<div class="abs product" style="left:600px;top:1915px"><div class="pic"><div role="img" aria-label="Vape device on dark stone" style="background:radial-gradient(circle at 50% 50%,#6f7a80,#2e3436 55%,#0c0c0c)"></div></div><div class="name">Halden X</div><div class="meta"><span><i class="coin">$</i>19.99</span><span><svg width="18" height="16" viewBox="0 0 24 22"><path d="M1 2h4l3 12h12l3-9H7" fill="none" stroke="#d4861f" stroke-width="2"/><circle cx="10" cy="19" r="2" fill="#d4861f"/><circle cx="18" cy="19" r="2" fill="#d4861f"/></svg>Buy Now</span></div></div>
<div class="abs product" style="left:839px;top:1915px"><div class="pic"><div role="img" aria-label="Boxed e-liquids on wooden crate" style="background:linear-gradient(160deg,#6aa6c4,#3b5566 45%,#7a5a2a 75%,#1a1208)"></div></div><div class="name">Kiwavape</div><div class="meta"><span><i class="coin">$</i>19.99</span><span><svg width="18" height="16" viewBox="0 0 24 22"><path d="M1 2h4l3 12h12l3-9H7" fill="none" stroke="#d4861f" stroke-width="2"/><circle cx="10" cy="19" r="2" fill="#d4861f"/><circle cx="18" cy="19" r="2" fill="#d4861f"/></svg>Buy Now</span></div></div>

<!-- about -->
<h2 class="abs heading slab" style="top:2375px"><span class="dot"></span><span>About <span style="color:#c9791a">Copper and Slate Mist NZ</span></span></h2>
<div class="abs about-copy">
  <p>Lorem ipsum dolor sit amet, consectetur adipiscing elit, sed do eiusmod tem por incididunt ut labore et dolore magna aliqua. Ut enim ad minim veniam, quis nostrud exercitation ullamco laboris nisi ut aliquip ex ea commodo con sequat.</p>
  <p>Duis aute irure dolor in reprehenderit in voluptate velit esse cillum dolore eu fugiat nulla pariatur. Excepteur sint occaecat cupidatat non proident, sunt in culpa qui officia deserunt mollit anim id est laborum.</p>
</div>
<a class="abs btn" style="left:113px;top:2703px;width:199px;height:48px;font-size:16px">Learn more</a>
<div class="abs about-photo"><div role="img" aria-label="Two rottweilers resting on a sofa"></div></div>

<!-- contact -->
<section class="abs contact" role="img" aria-label="Dark smoky silhouette backdrop"></section>
<h2 class="abs heading slab" style="top:2936px"><span class="dot"></span><span>Contact <span style="color:#c9791a">Us</span></span></h2>
<div class="abs field" style="left:113px;top:3035px;width:315px">Your Name</div>
<div class="abs field" style="left:443px;top:3035px;width:312px">Your Email</div>
<div class="abs field" style="left:770px;top:3035px;width:317px">Your Subject</div>
<div class="abs field" style="left:113px;top:3095px;width:974px;height:133px">Message</div>
<a class="abs btn" style="left:503px;top:3246px;width:197px;height:48px;font-size:16px">Submit</a>

<!-- footer -->
<footer class="abs footer"></footer>
<div class="abs foot-dot">Copper and Slate Mist NZ</div>
<div class="abs col" style="left:337px;top:3455px"><h4>Quick Links</h4><ul><li>Home</li><li>About</li><li>Products</li><li>Special Offer</li><li>Best Sellers</li><li>Contact</li></ul></div>
<div class="abs col" style="left:500px;top:3455px"><h4>Shop</h4><ul><li>E-Juice</li><li>Devices</li><li>Tanks &amp; Coils</li><li>Batteries</li><li>Rebuildables</li><li>Accessories</li></ul></div>
<div class="abs col" style="left:667px;top:3455px"><h4>Info</h4><ul><li>Terms &amp; Conditions</li><li>Returns</li><li>Privacy Policy</li></ul></div>
<div class="abs callbox">
  <div class="t">CONTACT US TODAY</div>
  <div class="n"><svg width="26" height="26" viewBox="0 0 24 24"><circle cx="12" cy="12" r="11" fill="none" stroke="#fff" stroke-width="1.8"/><path fill="#fff" d="M8.6 10.4a8 8 0 0 0 3.9 3.9l1.3-1.3a.6.6 0 0 1 .6-.15 6.6 6.6 0 0 0 2.1.35.6.6 0 0 1 .6.6v2.1a.6.6 0 0 1-.6.6A10 10 0 0 1 6.6 6.6.6.6 0 0 1 7.2 6h2.1a.6.6 0 0 1 .6.6c0 .7.1 1.4.35 2.1a.6.6 0 0 1-.15.6z"/></svg>1800.555.0142</div>
  <div class="s">Available from 9 am to 5 pm EST</div>
</div>
<div class="abs rule"></div>
<div class="abs copyright">COPYRIGHT © 2019 COPPER AND SLATE MIST NZ. ALL RIGHTS RESERVED.</div>

</body>
</html>
```